Redesign of existing site - Velbrin GmbH

Redesign of the following site.
https://www.velbrin-gmbh.example/

The colors red and green need to remain.
Topic: calendar binder

The font "FF Market Regular" should be used s well. But -- if you find a font which is similar and a bit more modern, then go with it. (see font-example.jpg)

The mainpage should have a slider with a video first. Enclosed is a screenshot of the video. (see video.jpg)

Logo also enclosed as svg. The red color might not be quit right. Please check it on your own.
For the second page this page should be used to redesign:
https://www.velbrin-gmbh.example/bindungen/ring-wire-bindung/

I am planing to use the DIVI builder. If you built this in DIVI builder and be able to send me the template or installation (Duplicator) that would be a huge advantage.
Updates

IMPORTANT:
I have received many designs in English. But I can't present them to the customer. Please convert them into German, otherwise they cannot be used.

Requirements
Must have
• Please translate designs into german if it is to be considered. How should I explain a design in english to the customer?

```html
<!DOCTYPE html>
<html lang="de">
<head>
<meta charset="utf-8">
<title>Velbrin GmbH – Kalenderbindungen</title>
<link href="https://fonts.googleapis.com/css2?family=Oswald:wght@400;500;600&family=Kaushan+Script&family=Montserrat:wght@400;500;600&display=swap" rel="stylesheet">
<style>
:root{
  --green:#6cbf2c;
  --green-dark:#5aa61f;
  --red:#ee1c1c;
  --black:#0a0a0a;
  --text:#333;
  --ink:#111;
  --muted:#555;
  --light:#f3f3f3;
  --white:#fff;
}
*{box-sizing:border-box;margin:0;padding:0}
html,body{width:1200px;height:3861px;overflow:hidden}
body{position:relative;background:var(--white);font-family:"Montserrat",sans-serif;color:var(--text)}
.abs{position:absolute}
.script{font-family:"Kaushan Script",cursive;font-weight:400}

/* header */
.site-header{left:0;top:0;width:1200px;height:113px;background:var(--white)}
.brand{left:141px;top:38px;font-family:"Montserrat",sans-serif;font-weight:600;font-size:30px;line-height:36px;color:var(--ink)}
.main-nav{right:150px;top:46px;display:flex;gap:33px;font-family:"Oswald",sans-serif;font-size:15px;letter-spacing:.5px;color:#222}
.main-nav svg{margin-top:3px}

/* hero */
.hero{left:0;top:113px;width:1200px;height:567px;overflow:hidden}
.hero-photo{left:0;top:0;width:1200px;height:567px;background:linear-gradient(100deg,#3c3a37 0%,#6b6863 35%,#a9a59c 60%,#8e8b84 80%,#5b5954 100%)}
.hero-title{left:141px;top:145px;font-family:"Oswald",sans-serif;font-weight:500;font-size:48px;line-height:60px;color:var(--white);letter-spacing:.5px}
.btn{display:inline-flex;align-items:center;justify-content:center;font-family:"Oswald",sans-serif;font-weight:500;font-size:13px;color:var(--white);letter-spacing:.3px}
.btn-green{left:141px;top:292px;width:212px;height:49px;background:var(--green);border-radius:3px}
.btn-red{background:var(--red);border-radius:3px}
.video-link{left:375px;top:295px;display:flex;align-items:center;gap:10px;color:var(--white);font-size:13px}
.play{width:42px;height:42px;border-radius:50%;background:var(--red);display:flex;align-items:center;justify-content:center}
.hero-slant{left:0;top:0}

/* intro */
.intro-title{left:0;width:1200px;top:710px;text-align:center;font-size:35px;color:var(--green)}
.intro-text{left:190px;width:820px;top:772px;text-align:center;font-size:12px;line-height:22px;color:var(--muted)}
.feature{top:846px;width:285px;height:333px;border:2px solid #ddd;border-radius:6px;background:var(--white)}
.feature-inner{position:absolute;left:-2px;top:70px;width:285px;height:200px;background:var(--white);box-shadow:0 14px 30px rgba(0,0,0,.08)}
.feature-icon{position:absolute;left:91px;top:20px;width:100px;height:100px;border-radius:50%;background:var(--green);display:flex;align-items:center;justify-content:center}
.feature h3{position:absolute;left:0;width:100%;top:136px;text-align:center;font-weight:500;font-size:18px;color:#111}
.feature p{position:absolute;left:28px;right:28px;top:172px;text-align:center;font-size:12px;line-height:22px;color:var(--muted)}
.more{font-weight:600;font-size:12px;color:var(--green);letter-spacing:.3px}
.feature .more{position:absolute;left:0;width:100%;top:294px;text-align:center}

/* bindings */
.bind-band{left:0;top:1270px;width:1200px;height:375px;background:linear-gradient(90deg,#6fc032 0%,#7fc84a 55%,#5fb52a 100%)}
.bind-title{left:141px;top:1350px;font-size:30px;color:var(--white)}
.bind-sub{left:143px;top:1410px;font-size:12px;color:#eef8e6}
.arrow-btn{top:1372px;width:42px;height:42px;border-radius:50%;display:flex;align-items:center;justify-content:center;color:var(--white);font-size:18px}
.arrow-prev{left:965px;border:1px solid rgba(255,255,255,.8)}
.arrow-next{left:1017px;background:var(--red)}
.bind-card{top:1462px;width:290px;height:340px;border-radius:4px;overflow:hidden}
.bind-card .label{position:absolute;left:0;bottom:0;height:52px;width:235px;background:#2a2a2a;clip-path:polygon(0 0,82% 0,100% 100%,0 100%);color:var(--white);font-family:"Kaushan Script",cursive;font-size:19px;padding:14px 0 0 24px}

/* stats */
.stat{top:1900px;width:286px;height:250px;background:linear-gradient(180deg,#fff 0%,#eaf6e0 45%,#fff 100%);text-align:center;color:#111}
.stat .s{font-family:"Kaushan Script",cursive;font-size:30px;line-height:44px}
.stat .n{font-family:"Oswald",sans-serif;font-weight:600;font-size:48px;line-height:54px;color:var(--green)}
.stat .n small{font-size:24px;color:#111;font-weight:500}

/* join */
.join{left:0;top:2250px;width:1200px;height:450px;overflow:hidden}
.join-photo{left:0;top:0;width:1200px;height:450px;background:linear-gradient(90deg,#d7dde4 0%,#b9c4cf 45%,#7d8fa5 70%,#aeb9c6 100%)}
.join-circle{left:35px;top:-35px;width:500px;height:500px;border-radius:50%;background:var(--green)}
.join-title{left:141px;top:80px;font-size:44px;line-height:66px;color:var(--white)}
.join-text{left:142px;top:232px;font-size:16px;line-height:25px;color:var(--white)}
.join-btn{left:141px;top:308px;width:198px;height:49px}

/* gallery */
.gal-title{left:0;width:1200px;top:2768px;text-align:center;font-size:36px;color:var(--green)}
.tile{top:2858px;width:226px;height:302px;background:#ececec;overflow:hidden}
.tile .img{position:absolute;left:0;width:226px;height:226px}
.tile .cap{position:absolute;left:0;width:226px;text-align:center}
.tile .cap .t{font-family:"Kaushan Script",cursive;font-size:19px;color:var(--green)}
.tile .cap .c{font-size:15px;color:#333;margin-top:2px}

/* landscape + footer */
.landscape{left:0;top:3175px;width:1200px;height:300px;background:linear-gradient(180deg,#ffffff 0%,#e6e9e3 30%,#b8bfae 70%,#9aa38c 100%)}
.footer{left:0;top:3430px;width:1200px;height:431px;background:var(--black);color:#ddd}
.f-head{font-family:"Kaushan Script",cursive;font-size:20px;color:var(--white)}
.f-rule{width:34px;height:2px;background:var(--green);margin-top:6px}
.f-text{font-size:12px;line-height:21px;color:#ccc}
.f-links{list-style:none;font-size:12px;line-height:25.5px;color:#ccc}
.f-links li::before{content:"• ";color:#fff}
.c-row{display:flex;gap:10px;margin-bottom:14px}
.c-row b{display:block;color:var(--white);font-weight:600;font-size:12px;line-height:18px}
.c-row span{font-size:12px;line-height:18px;color:#ccc}
.f-brand{left:886px;top:150px;font-family:"Montserrat",sans-serif;font-weight:600;font-size:36px;color:var(--white)}
.f-bottom{left:141px;top:3814px;width:918px;display:flex;justify-content:space-between;font-size:11px;color:#ccc}
.f-line{left:0;top:3793px;width:1200px;height:1px;background:#2a2a2a}
</style>
</head>
<body>

<header class="abs site-header">
  <div class="abs brand">Velbrin</div>
  <nav class="abs main-nav">
    <span>HOME</span><span>UNTERNEHMEN</span><span>BINDUNGEN</span><span>EXKLUSIVES</span><span>GALERIE</span><span>SERVICE</span><span>KONTAKT</span>
    <svg width="12" height="12" viewBox="0 0 12 12"><circle cx="5" cy="5" r="3.6" fill="none" stroke="#222" stroke-width="1.8"/><line x1="7.6" y1="7.6" x2="11" y2="11" stroke="#222" stroke-width="1.8"/></svg>
  </nav>
</header>

<section class="abs hero">
  <div class="abs hero-photo" role="img" aria-label="Foto einer Bindemaschine in der Produktion"></div>
  <h1 class="abs hero-title">RING-WIRE-BINDUNGEN,<br>SPIRALBINDUNGEN U.V.M</h1>
  <a class="abs btn btn-green">JETZT ANGEBOT ANFORDERN</a>
  <div class="abs video-link">
    <span class="play"><svg width="12" height="14" viewBox="0 0 12 14"><path d="M1 1 L11 7 L1 13 Z" fill="#fff"/></svg></span>
    Video Ansehen
  </div>
  <svg class="abs hero-slant" width="1200" height="567" viewBox="0 0 1200 567">
    <polygon points="0,567 740,484 1200,547 1200,567" fill="#fff"/>
    <polygon points="0,490 320,531 0,567" fill="var(--red)"/>
    <polygon points="740,484 1200,440 1200,547" fill="var(--green)"/>
  </svg>
</section>

<h2 class="abs intro-title script">Service aus einer Hand – Kompetenz verbindet!</h2>
<p class="abs intro-text">Velbrin - der Name steht für ein Höchstmaß an Qualität und Erfahrung bei allen planliegenden Kalender- und Broschürenbindungen. Seit über 50 Jahren beraten wir Kunden im In- und Ausland ideenreich bei allen Fragen rund um Design und Funktion ihrer Produkte.</p>

<article class="abs feature" style="left:141px">
  <div class="feature-inner"></div>
  <div class="feature-icon"><svg width="46" height="46" viewBox="0 0 46 46" fill="none" stroke="#fff" stroke-width="2"><circle cx="23" cy="18" r="13"/><circle cx="23" cy="18" r="8"/><path d="M15 29 L11 42 L17 39 L20 44 L23 32 M31 29 L35 42 L29 39 L26 44 L23 32"/></svg></div>
  <h3>Exklusives</h3>
  <p>Außergewöhnliche Herausforderungen sind unsere Spezialität - Exklusivität ist unser Markenzeichen.</p>
  <span class="more">ERFAHREN SIE MEHR ↗</span>
</article>
<article class="abs feature" style="left:457px">
  <div class="feature-inner"></div>
  <div class="feature-icon"><svg width="50" height="40" viewBox="0 0 50 40" fill="none" stroke="#fff" stroke-width="2"><circle cx="25" cy="12" r="7"/><circle cx="10" cy="16" r="5"/><circle cx="40" cy="16" r="5"/><path d="M13 38 V28 a12 10 0 0 1 24 0 V38 M2 38 V30 a8 7 0 0 1 9 -6 M48 38 V30 a8 7 0 0 0 -9 -6"/></svg></div>
  <h3>Unser Team</h3>
  <p>Seit über 50 Jahren beraten wir Kunden im In- und Ausland - ideenreich bei allen Fragen rund um Design und Funktion Ihrer Produkte.</p>
  <span class="more">ERFAHREN SIE MEHR ↗</span>
</article>
<article class="abs feature" style="left:774px">
  <div class="feature-inner"></div>
  <div class="feature-icon"><svg width="44" height="46" viewBox="0 0 44 46" fill="none" stroke="#fff" stroke-width="2"><rect x="6" y="4" width="28" height="36" rx="2"/><circle cx="14" cy="14" r="4"/><line x1="21" y1="12" x2="29" y2="12"/><line x1="21" y1="17" x2="29" y2="17"/><line x1="11" y1="24" x2="29" y2="24"/><line x1="11" y1="29" x2="25" y2="29"/><circle cx="34" cy="37" r="6"/></svg></div>
  <h3>Technische Informationen</h3>
  <p>Wenns mal ins Detail gehn soll, stehen wir Ihnen mit Rat zur Seite. Damit Sie optimale Produkte vorzeigen können.</p>
  <span class="more">ERFAHREN SIE MEHR ↗</span>
</article>

<section class="abs bind-band" role="img" aria-label="Grüner Hintergrund mit Spiralbindung"></section>
<h2 class="abs bind-title script">Die Leichtigkeit des Blätterns!</h2>
<p class="abs bind-sub">Unsere Kalenderbindungen und Bindungen im Überblick.</p>
<span class="abs arrow-btn arrow-prev">‹</span>
<span class="abs arrow-btn arrow-next">›</span>

<div class="abs bind-card" style="left:141px;background:linear-gradient(135deg,#2b2b2b,#c46a1a 50%,#333)" role="img" aria-label="Foto einer orangen Ring-Wire-Bindung"><div class="label">Ring-Wire-Bindung</div></div>
<div class="abs bind-card" style="left:455px;background:linear-gradient(135deg,#eef1f4,#8a939c 55%,#e9ecef)" role="img" aria-label="Foto einer Spiralbindung"><div class="label">Spiralbindung</div></div>
<div class="abs bind-card" style="left:769px;background:linear-gradient(135deg,#b01818,#e8e8ea 45%,#b41a1a 70%,#dcdde0)" role="img" aria-label="Foto roter Leinenfälzel"><div class="label">Leinenfälzel</div></div>
<div class="abs bind-card" style="left:1083px;background:linear-gradient(135deg,#6b6b6b,#e6ecf3 50%,#3a66b0)" role="img" aria-label="Foto eines Klappfälzel-Kalenders"><div class="label">Klappfälzel</div></div>

<div class="abs stat" style="left:141px"><div style="height:62px"></div><div class="s">Over</div><div class="n">56+</div><div class="s">Years of experience</div></div>
<div class="abs stat" style="left:457px"><div style="height:62px"></div><div class="s">Satisfied</div><div class="n">1547+</div><div class="s">Customers</div></div>
<div class="abs stat" style="left:774px"><div style="height:62px"></div><div class="s">More Than</div><div class="n">65 <small>Million+</small></div><div class="s">Bonds</div></div>

<section class="abs join">
  <div class="abs join-photo" role="img" aria-label="Foto eines Handschlags über einem Schreibtisch"></div>
  <div class="abs join-circle"></div>
  <h2 class="abs join-title script">Offen für neue<br>Herausforderungen</h2>
  <p class="abs join-text">Lassen Sie uns darüber sprechen, wie ich Ihrem<br>Team einen Mehrwert bieten kann</p>
  <a class="abs btn btn-red join-btn">BEWERBEN SIE SICH JETZT!</a>
</section>

<h2 class="abs gal-title script">Fotogalerie</h2>
<div class="abs tile" style="left:142px"><div class="img" style="top:0;background:linear-gradient(180deg,#9c8a70,#e8e4dc 40%,#cfd8c8)" role="img" aria-label="Foto eines Wandkalenders"></div><div class="cap" style="top:238px"><div class="t">Kalender</div><div class="c">23 BILDER</div></div></div>
<div class="abs tile" style="left:372px"><div class="cap" style="top:10px"><div class="t">Bücher u. lose Blattwerke</div><div class="c">36 BILDER</div></div><div class="img" style="top:76px;background:linear-gradient(160deg,#9aa0a6,#2f3135 55%,#b05a6a)" role="img" aria-label="Foto gebundener Notizbücher"></div></div>
<div class="abs tile" style="left:602px"><div class="img" style="top:0;background:linear-gradient(135deg,#f4f4f4,#b78453 50%,#e8e8e8)" role="img" aria-label="Foto eines exklusiven Kartonbuchs"></div><div class="cap" style="top:238px"><div class="t">Exklusives</div><div class="c">35 BILDER</div></div></div>
<div class="abs tile" style="left:833px"><div class="cap" style="top:10px"><div class="t">Produktion</div><div class="c">40 BILDER</div></div><div class="img" style="top:76px;background:linear-gradient(180deg,#f1efe8,#c9bca6 50%,#8f7f6c)" role="img" aria-label="Foto der Produktionshalle"></div></div>

<div class="abs landscape" role="img" aria-label="Luftbild einer Ortschaft mit Feldern"></div>
<svg class="abs" style="left:0;top:3340px" width="1200" height="140" viewBox="0 0 1200 140">
  <polygon points="0,35 470,85 0,135" fill="var(--green)"/>
  <polygon points="1200,20 1200,90 830,80" fill="var(--red)"/>
  <polygon points="0,135 470,85 830,80 1200,90 1200,140 0,140" fill="var(--black)"/>
</svg>

<footer class="abs footer">
  <div class="abs" style="left:141px;top:92px;width:250px">
    <div class="f-head">Über Velbrin</div><div class="f-rule"></div>
    <p class="f-text" style="margin-top:16px">Der Druckweiterverarbeiter Velbrin ist eine der größten Kalender-fabriken Deutschlands mit vier vollautomatischen Kalenderstraßen.</p>
    <p class="f-text" style="margin-top:6px">Als industrieller Buchbinder fertigt Velbrin großformatige Kalender bis 1,60 m Länge.</p>
    <p class="more" style="margin-top:12px">ERFAHREN SIE MEHR ↗</p>
  </div>
  <div class="abs" style="left:430px;top:92px">
    <div class="f-head">Schnell Links</div><div class="f-rule"></div>
    <ul class="f-links" style="margin-top:12px"><li>Home</li><li>Unternehmen</li><li>Bindungen</li><li>Exklusives</li><li>Galerie</li><li>Service</li><li>Kontakt</li></ul>
  </div>
  <div class="abs" style="left:584px;top:92px">
    <div class="f-head">Kontaktdaten</div><div class="f-rule"></div>
    <div style="margin-top:16px">
      <div class="c-row"><svg width="12" height="16" viewBox="0 0 12 16"><path d="M6 1a5 5 0 0 1 5 5c0 4-5 9-5 9S1 10 1 6a5 5 0 0 1 5-5z" fill="#fff"/><circle cx="6" cy="6" r="2" fill="#000"/></svg><div><b>Adresse</b><span>Velbrin GmbH &amp; Co. KG<br>Lindenweg 14 84100 Musterbach</span></div></div>
      <div class="c-row"><svg width="12" height="14" viewBox="0 0 12 14"><path d="M2 1 L5 1 L6 4 L4 5.5 Q5.5 8.5 7.5 10 L9 8 L12 9 L12 12 Q6 13 2 8 Q0 4 2 1z" fill="#fff"/></svg><div><b>Telefon</b><span>+49 (0000) 5550-0</span></div></div>
      <div class="c-row"><svg width="13" height="12" viewBox="0 0 13 12"><rect x="0.5" y="1.5" width="12" height="9" fill="#fff"/><path d="M0.5 1.5 L6.5 7 L12.5 1.5" fill="none" stroke="#000"/></svg><div><b>E-Mail</b><span>info@velbrin-gmbh.example</span></div></div>
    </div>
  </div>
  <div class="abs f-brand">Velbrin</div>
</footer>
<div class="abs f-line"></div>
<div class="abs f-bottom"><span>© 2025 Velbrin GmbH &amp; Co. KG. Alle Rechte vorbehalten.</span><span>Imprint &nbsp; | &nbsp; Cookies &nbsp; | &nbsp; Privacy Policy</span></div>

</body>
</html>
```